Corwell Holdings Business Cards

Hello. I need business cards designed with our new logo. I'd like to see at least 3 different designs. At least one with a dark background, and at least one with a white background. Maybe one with gray or blue for the background. Play with gradient colors and maybe even insert a pic of a skyline in the background of one or more of them. Use your judgement. We will need 2 cards printed. They need to accommodate the employee name, title, company address, phone, email, and website. Thanks.

Target Market(s)

Wealthy mature investors.

Contact Information for Business Card

Single-sided, professional, clean design that incorporates our logo.

Font styles to use
Sans Serif

Requirements
Must have
• Our new logo needs to be featured on it. (See attached.)
• Employee Name (In all CAPS)
• Title
• Street Address, City, ST Zip Code
• Cell Phone #, Email Address, Website Address
Nice to have
• Design that blends well with our new logo and its colors, or a city scape or other graphic design that looks like an apartment complex in the background. Blues and grays are nice, but use your judgement.
Should not have
• Modern or oriental looking designs or bright colors.

```html
<!DOCTYPE html>
<html lang="en">
<head>
<meta charset="utf-8">
<title>Corwell Holdings Business Cards</title>
<link rel="stylesheet" href="https://fonts.googleapis.com/css2?family=Montserrat:wght@400;500;700&family=Source+Sans+3:wght@400&display=swap">
<style>
  :root {
    --page-bg: #ececec;
    --card-white: #ffffff;
    --card-white-shade: #f1f1f1;
    --brand-blue: #29a3dc;
    --brand-blue-deep: #2499d0;
    --ink-gray: #555659;
    --ink-dark: #4a4b4e;
    --on-blue: #ffffff;
  }
  * { margin: 0; padding: 0; box-sizing: border-box; }
  html, body { width: 1200px; height: 1176px; overflow: hidden; }
  body { background: var(--page-bg); position: relative; font-family: "Source Sans 3", Arial, sans-serif; }

  .card {
    position: absolute;
    left: 229px;
    width: 724px;
    height: 414px;
    border-radius: 22px;
    overflow: hidden;
  }
  .card--front {
    top: 125px;
    background: linear-gradient(135deg, var(--card-white) 40%, var(--card-white-shade) 100%);
  }
  .card--back {
    top: 597px;
    background: linear-gradient(135deg, var(--brand-blue-deep) 0%, var(--brand-blue) 100%);
  }

  .wordmark {
    position: absolute;
    font-family: "Montserrat", Arial, sans-serif;
    font-weight: 500;
    line-height: 1;
  }
  .wordmark__main { display: block; letter-spacing: 1px; }
  .wordmark__sub { display: block; letter-spacing: 1.5px; }

  .card--front .wordmark { left: 67px; top: 182px; color: var(--brand-blue); }
  .card--front .wordmark__main { font-size: 36px; }
  .card--front .wordmark__sub { font-size: 17px; margin-top: 6px; }

  .card--back .wordmark { left: 0; right: 0; top: 168px; text-align: center; color: var(--on-blue); }
  .card--back .wordmark__main { font-size: 48px; }
  .card--back .wordmark__sub { font-size: 24px; margin-top: 8px; }

  .divider {
    position: absolute;
    left: 361px;
    top: 105px;
    width: 2px;
    height: 207px;
    background: var(--brand-blue);
  }

  .contact { position: absolute; left: 389px; top: 112px; color: var(--ink-gray); }
  .contact__name {
    font-family: "Montserrat", Arial, sans-serif;
    font-weight: 400;
    font-size: 26px;
    color: var(--ink-gray);
    letter-spacing: 0.3px;
    line-height: 1.1;
  }
  .contact__name strong { font-weight: 700; color: var(--ink-dark); }
  .contact__licence { font-size: 17px; color: var(--brand-blue); margin-top: 3px; }
  .contact__list { list-style: none; margin-top: 22px; }
  .contact__item { display: flex; align-items: center; font-size: 17.5px; height: 23px; }
  .contact__icon { width: 16px; height: 16px; margin-right: 8px; fill: var(--brand-blue); }
  .contact__address { font-size: 17.5px; margin-top: 16px; }
</style>
</head>
<body>

<section class="card card--front" aria-label="Card front">
  <div class="wordmark">
    <span class="wordmark__main">CORWELL</span>
    <span class="wordmark__sub">HOLDINGS, LLC</span>
  </div>

  <div class="divider"></div>

  <div class="contact">
    <p class="contact__name">YOUR <strong>NAME</strong></p>
    <p class="contact__licence">CA LIC/ #582306</p>
    <ul class="contact__list">
      <li class="contact__item">
        <svg class="contact__icon" viewBox="0 0 16 16" aria-hidden="true"><path d="M1 6c0-2 3-3 7-3s7 1 7 3v1.5h-3.5V6h-7v1.5H1zM4 8l1.5-2h5L12 8v5H4z"/><circle cx="8" cy="10" r="1.6" fill="#fff"/></svg>
        000 000 0000
      </li>
      <li class="contact__item">
        <svg class="contact__icon" viewBox="0 0 16 16" aria-hidden="true"><path d="M1 3.5h14v9H1z"/><path d="M1.5 4l6.5 5 6.5-5" fill="none" stroke="#fff" stroke-width="1.2"/></svg>
        name@corwellmail.com
      </li>
      <li class="contact__item">
        <svg class="contact__icon" viewBox="0 0 16 16" aria-hidden="true"><g fill="none" stroke="var(--brand-blue)" stroke-width="1.1"><circle cx="8" cy="8" r="6.5"/><ellipse cx="8" cy="8" rx="3" ry="6.5"/><path d="M1.5 8h13M2.5 4.8h11M2.5 11.2h11"/></g></svg>
        www.corwellholdings.com
      </li>
    </ul>
    <p class="contact__address">Street Address, City, ST Zip Code</p>
  </div>
</section>

<section class="card card--back" aria-label="Card back">
  <div class="wordmark">
    <span class="wordmark__main">CORWELL</span>
    <span class="wordmark__sub">HOLDINGS, LLC</span>
  </div>
</section>

</body>
</html>
```